Get referrals for Insurance customers and the domain name is tallyhopper.ca We are an insurance

We need a logo and a website for a referral site. Our advertising and promotion will send customers to this website where they will fill out a form giving their information as well as person they want to refer. The logo idea that I have is a gear with a dollar sign in it the number 2 and the letter U. Another words dollars to you. If this can be animated with sounds, that would be great. Once this form is filled in it goes to a referral software site such as Bounty Pebble or Gainbrook where the data is saved for us to follow up. This is not a complicated site. It will reassure the people who will refer their friends, family members or other aquiatnces that we will provide great service to and best prices for home and business insurance. It will exclude auto insurance as not referral for a monitory reward(regulations). The reward will be $100 for business and house insurance and $25 condo or townhome insurance. It will imply that this $100 is limited time offer. The site should be set so that we could edit the website once the designer has given it to us. The people we expecting to be our referrers are real estate agents, notaries public, and our existing customers.

The designs are not what I was expecting. Is there any way I can communicate with the designer that I think made the best attempt at what I was expecting?

Target Market(s)

Our customers, realtors, notaries public and anyone who knows

Industry/Entity Type

Insurance Broker

Logo Text

Dollar sign, Gear, number 2 and U a funnel. Dollars to you . See what you can

Number of Pages Required

4 page

Font styles to use
Other font styles liked:
• Calibri

Colors
0455a3
ec1f27
ffffff

Requirements
Must have
• Fillable form on info about referer and the referred. This will data will be sent to the third party who will have our data for keeping track of the referrals and where Our referees can see how many people they have referred and who has been approved for payment. The third parties our such as Bounty Pebble or Gainbrook.
Nice to have
• Animated logo with sound would be nice. This will be used on the website only. We use maple crest insurance logo as seen on www,maplecrestinsurance.ca for all communications.
Should not have
• I have attached two files for reference only they do not have the exact text that I want to have on the website. I am working on that and it will always be changing to some extent. You can talk to me.

```html
<!DOCTYPE html>
<html lang="en">
<head>
<meta charset="utf-8">
<title>Tally Hopper — Online Referral</title>
<link href="https://fonts.googleapis.com/css2?family=Open+Sans:wght@400;600;700&display=swap" rel="stylesheet">
<style>
:root{
  --blue:#0455a3;
  --red:#ec1f27;
  --white:#ffffff;
  --ink:#333a40;
  --muted:#7a8088;
  --light:#f1f1f1;
  --dark:#141e2b;
  --darker:#0f1823;
  --star:#f5a623;
}
*{box-sizing:border-box;margin:0;padding:0}
html,body{width:1200px;height:3854px;overflow:hidden}
body{font-family:"Open Sans",Calibri,Arial,sans-serif;color:var(--ink);background:var(--white);font-size:14px}
.wrap{width:932px;margin:0 auto;position:relative;height:100%}
section,header,footer{position:relative;overflow:hidden}

/* header */
.site-header{height:103px;background:var(--white)}
.brand{position:absolute;left:0;top:30px;display:flex;align-items:center;gap:12px}
.brand-dot{width:42px;height:42px;border-radius:50%;background:var(--blue)}
.brand-name{font-size:28px;font-weight:600;color:var(--blue)}
.main-nav{position:absolute;right:0;top:44px;display:flex;gap:26px;font-size:13px}
.main-nav a{color:var(--ink);text-decoration:none}
.main-nav a.active{color:var(--red)}

/* hero */
.hero{height:509px;background:linear-gradient(180deg,#d9c6a8 0%,#b99a7a 35%,#7ea55a 70%,#4f8a32 100%)}
.hero-arrow{position:absolute;top:235px;width:32px;height:32px;border-radius:50%;background:rgba(255,255,255,.85);display:flex;align-items:center;justify-content:center}
.hero-arrow.prev{left:40px}.hero-arrow.next{right:40px}

/* referral form */
.referral{height:588px;background:var(--red);color:var(--white)}
.referral h2{position:absolute;left:0;right:0;top:22px;text-align:center;font-size:27px;font-weight:600}
.form-col{position:absolute;top:68px}
.form-col.you{left:0;width:400px}
.form-col.friend{left:532px;width:400px}
.form-col h3{font-size:17px;font-weight:600;margin-bottom:12px}
.field{background:var(--white);height:40px;color:#555;font-size:12px;padding:0 12px;display:flex;align-items:center;margin-bottom:12px}
.field-row{display:flex;gap:14px}
.field-row .field{flex:1}
.opt-line{font-size:13px;display:flex;align-items:center;gap:10px;margin:8px 0}
.box{display:inline-block;width:10px;height:10px;background:var(--white);margin-right:6px;vertical-align:-1px}
.bonus{font-size:13px;line-height:1.7;margin-top:10px}
.bonus .indent{padding-left:107px}
.fine{font-size:9px;line-height:1.45;opacity:.85;margin-top:8px}
.contact-me{font-size:13px;line-height:1.35;display:flex;gap:14px;margin-bottom:18px}
.submit{position:absolute;left:414px;top:524px;width:106px;height:38px;background:#2a2a2a;color:var(--white);font-size:12px;font-weight:600;display:flex;align-items:center;justify-content:center;letter-spacing:.5px}

/* welcome */
.welcome{height:458px;text-align:center}
.section-title{color:var(--red);font-size:27px;font-weight:600}
.welcome .section-title{position:absolute;left:0;right:0;top:72px}
.welcome p{position:absolute;left:0;right:0;top:118px;font-size:14px;line-height:1.6;color:var(--ink)}
.features{position:absolute;left:0;right:0;top:208px;display:flex;gap:20px}
.feature{flex:1;height:178px;background:var(--blue);color:var(--white);display:flex;flex-direction:column;align-items:center;justify-content:center;gap:16px;font-size:17px;line-height:1.35}

/* protection */
.protection{height:400px;background:linear-gradient(180deg,#4a6a8e 0%,#28415f 40%,#3b3a30 75%,#1f2b22 100%)}
.protect-box{position:absolute;left:0;top:95px;width:444px;height:206px;background:rgba(14,22,34,.85);color:var(--white);padding:22px 28px}
.protect-box h3{font-size:16px;font-weight:600;line-height:1.4;margin-bottom:14px}
.protect-box li{list-style:none;font-size:13.5px;display:flex;gap:12px;align-items:center;margin-bottom:12px}

/* partners */
.partners{height:202px;background:var(--light);text-align:center}
.partners .section-title{position:absolute;left:0;right:0;top:40px}
.partner-row{position:absolute;left:0;right:0;top:110px;display:flex;justify-content:space-between;align-items:center}
.partner{font-size:19px;font-weight:700;color:#2a2a2a;letter-spacing:1px}
.badge{width:52px;height:44px;border-radius:50%;background:#2a2a2a}

/* blog */
.blog{height:555px}
.blog-head{position:absolute;left:0;right:0;top:65px;display:flex;justify-content:center;align-items:center;gap:40px}
.nav-sq{width:24px;height:24px;border:1px solid #cfcfcf;display:flex;align-items:center;justify-content:center}
.cards{position:absolute;left:0;right:0;top:135px;display:flex;gap:22px}
.card{flex:1}
.card-img{height:178px}
.card h4{font-size:15px;font-weight:400;color:#222;line-height:1.35;margin:16px 0 10px}
.card p{font-size:10.5px;line-height:1.55;color:var(--muted)}
.meta{display:flex;gap:18px;font-size:10px;color:var(--muted);margin-top:16px;align-items:center}
.meta span{display:flex;gap:5px;align-items:center}

/* reviews */
.reviews{height:462px;background:var(--light);text-align:center}
.reviews .section-title{position:absolute;left:0;right:0;top:78px}
.review-row{position:absolute;left:0;right:0;top:132px;display:flex;gap:22px;text-align:left}
.review{flex:1}
.quote{background:var(--white);padding:20px 20px 22px 22px;font-size:11px;line-height:1.6;color:var(--muted);position:relative;height:142px}
.quote:after{content:"";position:absolute;right:46px;bottom:-12px;border-left:12px solid transparent;border-right:12px solid transparent;border-top:12px solid var(--white)}
.q-mark{color:#cfcfcf;font-size:30px;line-height:0;vertical-align:-12px;margin-right:6px}
.author{display:flex;justify-content:flex-end;align-items:center;gap:10px;margin-top:18px;padding-right:30px;font-size:12px}
.author small{color:var(--muted);font-size:9px}
.stars{color:var(--star);font-size:10px;letter-spacing:1px;text-align:right}
.avatar{width:34px;height:34px;background:#c9b8a6;border:2px solid var(--white)}
.dots{position:absolute;left:0;right:0;top:357px;display:flex;justify-content:center;gap:12px}
.dots i{width:7px;height:7px;border-radius:50%;background:#cfcfcf}
.dots i.on{background:#555}

/* cta */
.cta{height:242px;text-align:center}
.cta .section-title{position:absolute;left:0;right:0;top:70px;font-size:30px}
.cta-btn{position:absolute;left:50%;top:136px;transform:translateX(-50%);width:200px;height:46px;background:var(--blue);color:var(--white);font-size:16px;display:flex;align-items:center;justify-content:center}

/* footer */
.site-footer{height:328px;background:var(--dark);color:#aeb5bf;font-size:10.5px}
.foot-col{position:absolute;top:56px}
.foot-col h5{color:var(--white);font-size:14px;font-weight:600;margin-bottom:20px}
.foot-col.about{left:0;width:270px;line-height:1.65}
.foot-col.about b{color:var(--white)}
.foot-col.links{left:370px;width:330px}
.links-grid{display:grid;grid-template-columns:1fr 1fr 1fr;row-gap:9px}
.foot-col.contact{left:788px;width:160px}
.contact-line{display:flex;gap:10px;align-items:center;margin-bottom:10px}
.copyright{position:absolute;left:0;top:266px;font-size:10px}
.socials{position:absolute;right:0;top:256px;display:flex;gap:10px}
.socials i{width:28px;height:28px;border-radius:50%;border:1px solid #6b7380}
</style>
</head>
<body>

<header class="site-header">
  <div class="wrap">
    <div class="brand"><span class="brand-dot"></span><span class="brand-name">Tally Hopper</span></div>
    <nav class="main-nav">
      <a class="active" href="#">Home</a><a href="#">About Us</a><a href="#">Services</a><a href="#">Insurance Plans</a><a href="#">Blog</a><a href="#">Contact Us</a>
    </nav>
  </div>
</header>

<section class="hero" role="img" aria-label="Photo of a smiling family sitting on the lawn in front of their brick house">
  <span class="hero-arrow prev"><svg width="10" height="14" viewBox="0 0 10 14"><path d="M8 1L2 7l6 6" stroke="#333" stroke-width="2" fill="none"/></svg></span>
  <span class="hero-arrow next"><svg width="10" height="14" viewBox="0 0 10 14"><path d="M2 1l6 6-6 6" stroke="#333" stroke-width="2" fill="none"/></svg></span>
</section>

<section class="referral">
  <div class="wrap">
    <h2>Online Referral</h2>
    <div class="form-col you">
      <h3>You</h3>
      <div class="field">Name</div>
      <div class="opt-line">Agent :&nbsp; <span><i class="box"></i>Dana Pruitt</span><span><i class="box"></i>Mirela</span><span><i class="box"></i>Oskar</span></div>
      <div class="bonus">Referral Bonus :&nbsp; <i class="box"></i>$100 for business and house insurance<br><span class="indent"><i class="box"></i>$25 condo or townhome insurance.</span></div>
      <p class="fine">Offer valid for a limited time only. Rewards are paid once the referred client is approved.<br>Auto insurance referrals are not eligible for rewards.</p>
    </div>
    <div class="form-col friend">
      <h3>Your Friend</h3>
      <div class="contact-me"><i class="box"></i><span>Please Contact Me!<br>I am ready to save up to 40% on my insurance</span></div>
      <div class="field">Name</div>
      <div class="field">Address</div>
      <div class="field-row"><div class="field">City</div><div class="field">State</div><div class="field">Zip</div></div>
      <div class="field-row"><div class="field">Phone</div><div class="field">Email</div></div>
      <div class="opt-line">Best time to call :&nbsp; <span><i class="box"></i>AM</span><span><i class="box"></i>PM</span></div>
      <div class="bonus">Referral Bonus :&nbsp; <i class="box"></i>$100 for business and house insurance<br><span class="indent"><i class="box"></i>$25 condo or townhome insurance.</span></div>
      <p class="fine">Offer valid for a limited time only. Rewards are paid once the referred client is approved.<br>Auto insurance referrals are not eligible for rewards.</p>
    </div>
    <div class="submit">SUBMIT</div>
  </div>
</section>

<section class="welcome">
  <div class="wrap">
    <h2 class="section-title">Welcome to Tally Hopper</h2>
    <p>As a Real Estate Agent, you know that the closing process usually leaves buyers and sellers stressed to the max with nerves getting raw and<br>emotions flying high. You are your client's first point of contact and buffer when schedules grow tight - and as such, you want to provide<br>them with the best possible service to make this transaction proceed as smooth as possible.</p>
    <div class="features">
      <div class="feature">
        <svg width="30" height="34" viewBox="0 0 30 34"><rect x="1" y="1" width="28" height="32" rx="2" fill="none" stroke="#fff" stroke-width="2"/><rect x="6" y="6" width="18" height="6" fill="#fff"/><rect x="6" y="16" width="5" height="5" fill="#fff"/><rect x="13" y="16" width="5" height="5" fill="#fff"/><rect x="20" y="16" width="4" height="5" fill="#fff"/><rect x="6" y="24" width="5" height="5" fill="#fff"/><rect x="13" y="24" width="5" height="5" fill="#fff"/><rect x="20" y="24" width="4" height="5" fill="#fff"/></svg>
        <span>Assuring proper<br>coverage</span></div>
      <div class="feature">
        <svg width="34" height="30" viewBox="0 0 34 30"><rect x="1" y="7" width="32" height="22" rx="2" fill="#fff"/><path d="M11 7V3h12v4" stroke="#fff" stroke-width="2" fill="none"/><rect x="1" y="15" width="32" height="2" fill="#0455a3"/></svg>
        <span>Providing excellent<br>customer service</span></div>
      <div class="feature">
        <svg width="30" height="34" viewBox="0 0 30 34"><path d="M6 8h18l4 24H2z" fill="#fff"/><path d="M10 8a5 5 0 0 1 10 0" stroke="#fff" stroke-width="2" fill="none"/><text x="15" y="27" text-anchor="middle" font-size="13" font-weight="700" fill="#0455a3" font-family="Open Sans,sans-serif">$</text></svg>
        <span>Obtaining lowest<br>premium</span></div>
      <div class="feature">
        <svg width="22" height="34" viewBox="0 0 22 34"><rect x="1" y="1" width="20" height="32" rx="3" fill="none" stroke="#fff" stroke-width="2"/><rect x="4" y="5" width="14" height="21" fill="#fff"/><circle cx="11" cy="29.5" r="1.5" fill="#fff"/></svg>
        <span>Offering free mobile<br>service</span></div>
    </div>
  </div>
</section>

<section class="protection" role="img" aria-label="Photo of a lit house among pine trees at dusk with a city harbour behind">
  <div class="wrap">
    <div class="protect-box">
      <h3>We will provide the best protection for your client's new investment for</h3>
      <ul>
        <li><svg width="14" height="14" viewBox="0 0 14 14"><path d="M1 7l4 4 8-9" stroke="#fff" stroke-width="2" fill="none"/></svg>Single Family homes, Townhouse, Condominiums</li>
        <li><svg width="14" height="14" viewBox="0 0 14 14"><path d="M1 7l4 4 8-9" stroke="#fff" stroke-width="2" fill="none"/></svg>Rental/Investment properties</li>
        <li><svg width="14" height="14" viewBox="0 0 14 14"><path d="M1 7l4 4 8-9" stroke="#fff" stroke-width="2" fill="none"/></svg>Corporate ownership and/or multiple owners</li>
      </ul>
    </div>
  </div>
</section>

<section class="partners">
  <div class="wrap">
    <h2 class="section-title">Insurance Companies</h2>
    <div class="partner-row">
      <span class="partner">Ravel</span>
      <span class="partner">Halvern</span>
      <span class="badge"></span>
      <span class="partner">Osterly</span>
      <span class="partner">Kestrel</span>
      <span class="partner">Zizi</span>
      <span class="partner">Ramblor</span>
    </div>
  </div>
</section>

<section class="blog">
  <div class="wrap">
    <div class="blog-head">
      <span class="nav-sq"><svg width="8" height="10" viewBox="0 0 8 10"><path d="M6 1L2 5l4 4" stroke="#ec1f27" stroke-width="1.6" fill="none"/></svg></span>
      <h2 class="section-title">Blog</h2>
      <span class="nav-sq"><svg width="8" height="10" viewBox="0 0 8 10"><path d="M2 1l4 4-4 4" stroke="#ec1f27" stroke-width="1.6" fill="none"/></svg></span>
    </div>
    <div class="cards">
      <article class="card">
        <div class="card-img" role="img" aria-label="Photo of a couple reviewing documents at home" style="background:linear-gradient(135deg,#c9a070,#8a6a48)"></div>
        <h4>Donec scelerisque felis at ante rhoncus, non mattis nulla facilisis</h4>
        <p>Integer gravida risus risus, in imperdiet leo convallis sed. Aenean lobortis neque, vitae faucibus lorem. Nulla dignissim tempus nisi, sed lobortis velit faucibus at. Fusce vel rutrum erat. Vivamus blandit interdum egestas.</p>
        <div class="meta"><span>&#9829; (28)</span><span>&#9993; (21)</span><span>&#9719; 10 Oct, 2017</span></div>
      </article>
      <article class="card">
        <div class="card-img" role="img" aria-label="Photo of a modern house with a pool at dusk" style="background:linear-gradient(180deg,#4a5f78,#2f3d4d 55%,#4b86b0)"></div>
        <h4>Donec scelerisque felis at ante rhoncus, non mattis nulla facilisis</h4>
        <p>Integer gravida risus risus, in imperdiet leo convallis sed. Aenean lobortis neque, vitae faucibus lorem. Nulla dignissim tempus nisi, sed lobortis velit faucibus at. Fusce vel rutrum erat. Vivamus blandit interdum egestas.</p>
        <div class="meta"><span>&#9829; (28)</span><span>&#9993; (21)</span><span>&#9719; 10 Oct, 2017</span></div>
      </article>
      <article class="card">
        <div class="card-img" role="img" aria-label="Video still of a couple working on a laptop" style="background:linear-gradient(135deg,#ddd6cc,#a69a8a);display:flex;align-items:center;justify-content:center">
          <svg width="44" height="44" viewBox="0 0 44 44"><circle cx="22" cy="22" r="21" fill="rgba(0,0,0,.55)"/><path d="M17 13l13 9-13 9z" fill="#fff"/></svg>
        </div>
        <h4>Donec scelerisque felis at ante rhoncus, non mattis nulla facilisis</h4>
        <p>Integer gravida risus risus, in imperdiet leo convallis sed. Aenean lobortis neque, vitae faucibus lorem. Nulla dignissim tempus nisi, sed lobortis velit faucibus at. Fusce vel rutrum erat. Vivamus blandit interdum egestas.</p>
        <div class="meta"><span>&#9829; (28)</span><span>&#9993; (21)</span><span>&#9719; 10 Oct, 2017</span></div>
      </article>
    </div>
  </div>
</section>

<section class="reviews">
  <div class="wrap">
    <h2 class="section-title">Clients Reviews</h2>
    <div class="review-row">
      <div class="review">
        <div class="quote"><span class="q-mark">&ldquo;</span>Mauris quis sodales enim, semper ultrices massa. Pellentesque risus dolor, tristique vel facilisis at, laoreet ut elit. Fusce id augue et metus cursus pulvinar. In nec lectus porttitor, porttitor velit vel, tempus tortor.</div>
        <div class="author"><div><div>Dana Pruitt, <small>City name</small></div><div class="stars">&#9733;&#9733;&#9733;&#9733;&#9733;</div></div><span class="avatar" role="img" aria-label="Client portrait"></span></div>
      </div>
      <div class="review">
        <div class="quote"><span class="q-mark">&ldquo;</span>Mauris quis sodales enim, semper ultrices massa. Pellentesque risus dolor, tristique vel facilisis at, laoreet ut elit. Fusce id augue et metus cursus pulvinar. In nec lectus porttitor, porttitor velit vel, tempus tortor.</div>
        <div class="author"><div><div>Dana Pruitt, <small>City name</small></div><div class="stars">&#9733;&#9733;&#9733;&#9733;&#9733;</div></div><span class="avatar" role="img" aria-label="Client portrait"></span></div>
      </div>
      <div class="review">
        <div class="quote"><span class="q-mark">&ldquo;</span>Mauris quis sodales enim, semper ultrices massa. Pellentesque risus dolor, tristique vel facilisis at, laoreet ut elit. Fusce id augue et metus cursus pulvinar. In nec lectus porttitor, porttitor velit vel, tempus tortor.</div>
        <div class="author"><div><div>Dana Pruitt, <small>City name</small></div><div class="stars">&#9733;&#9733;&#9733;&#9733;&#9733;</div></div><span class="avatar" role="img" aria-label="Client portrait"></span></div>
      </div>
    </div>
    <div class="dots"><i class="on"></i><i></i><i></i><i></i></div>
  </div>
</section>

<section class="cta">
  <div class="wrap">
    <h2 class="section-title">Vestibulum condimentum, risus ut posuere cursus</h2>
    <div class="cta-btn">Get Started Now</div>
  </div>
</section>

<footer class="site-footer">
  <div class="wrap">
    <div class="foot-col about">
      <h5>About Us</h5>
      <p>Donec at enim elementum, sodales est nec, imperdiet nulla. Vivamus massa risus, iaculis sed nunc accumsan, iaculis pharetra dolor. Nulla non sem consequat, volutpat neque et, consectetur lectus. Duis tur vitae rutrum lacus. Pellentesque sed... <b>More</b></p>
    </div>
    <div class="foot-col links">
      <h5>Links</h5>
      <div class="links-grid">
        <span>Home</span><span>Blog</span><span>Forms</span>
        <span>About Us</span><span>Contact Us</span><span>Terms and Conditions</span>
        <span>Services</span><span>Referrals</span><span>Privacy Policy</span>
        <span>Insurance Plans</span><span>Request a Quote</span><span>Sitemap</span>
      </div>
    </div>
    <div class="foot-col contact">
      <h5>Contact Us</h5>
      <div class="contact-line"><svg width="10" height="12" viewBox="0 0 10 12"><path d="M2 1h2l1 3-1.5 1a6 6 0 0 0 2.5 3L7 6.5l3 1V10a1 1 0 0 1-1 1A8 8 0 0 1 1 3a1 1 0 0 1 1-2z" fill="#aeb5bf"/></svg>604 555 0142</div>
      <div class="contact-line"><svg width="12" height="9" viewBox="0 0 12 9"><rect x=".5" y=".5" width="11" height="8" fill="none" stroke="#aeb5bf"/><path d="M.5 .5l5.5 4.5 5.5-4.5" fill="none" stroke="#aeb5bf"/></svg>info@tallyhopper.ca</div>
    </div>
    <div class="copyright">Copyright &copy; 2017 &nbsp;Tally Hopper. &nbsp;All rights reserved.</div>
    <div class="socials"><i></i><i></i><i></i><i></i><i></i></div>
  </div>
</footer>

</body>
</html>
```